Building and Facilities Management brochure

Please refer to attached PDF, page by page with information about the brief.
SOPHISTICATED, BOLD, PROFESSIONAL BROCHURE to market our company in business meetings to Builders, Owners of buildings, Strata Committees etc.

The final design should portray quality, service, integrity,
Clear Communication

Attached is:
- pdf with details of basic layout options and wording and most of the information about the brief.
- Logo options to use
- Business card designs to understand what design we have previously had.
- Word document of the pdf if that helps to copy the information.

Target Market(s)

Professionals. Builders/developer, Strata Owners, and Building owners who want a high level of service and management of their building

Industry/Entity Type

It Company

Requirements
Must have
• - Logo
• - Contact details
• - Use of the colour in the design which has been specified.
• - Images/s of building/s
• - Use the phrase "Quality Service with Integrity"
Nice to have
• - as much of the wording as possible from the document which was uploaded, that will fit and work with the design
Should not have
• Excessive colour or variances as it needs to stay clear, bold and sophisticated.
• Too much on the page, clarity is key for clear communication without trying to clutter too much on the page.

```html
<!DOCTYPE html>
<html lang="en">
<head>
<meta charset="UTF-8">
<title>Northgate Building Services – Brochure Cover</title>
<link rel="stylesheet" href="https://fonts.googleapis.com/css2?family=Raleway:wght@200;500&display=swap">
<style>
  :root {
    --stage: #e4e4e4;
    --slate: #434b57;
    --slate-gloss: #4a535f;
    --gloss-edge: #9aa4b2;
    --sky-blue: #29a8dc;
    --band-white: #f1f3f5;
    --city-light: #d3e2ec;
    --city-mid: #86a5bc;
    --city-deep: #3f5f7d;
  }
  * { margin: 0; padding: 0; box-sizing: border-box; }
  html, body {
    width: 1200px;
    height: 818px;
    overflow: hidden;
    background: var(--stage);
  }
  .canvas {
    width: 1200px;
    height: 818px;
    display: flex;
    align-items: center;
    justify-content: center;
  }
  .brochure-cover {
    width: 523px;
    height: 740px;
    display: block;
  }
  .brand-name {
    font-family: "Raleway", sans-serif;
    font-weight: 500;
    font-size: 18px;
    letter-spacing: 3px;
    fill: var(--sky-blue);
  }
  .values-line {
    font-family: "Raleway", sans-serif;
    font-weight: 200;
    font-size: 50px;
    letter-spacing: 4px;
    fill: var(--slate-gloss);
    stroke: var(--gloss-edge);
    stroke-width: 0.9;
  }
</style>
</head>
<body>
<main class="canvas">
  <svg class="brochure-cover" viewBox="0 0 523 740" xmlns="http://www.w3.org/2000/svg">
    <defs>
      <linearGradient id="cityTones" x1="0" y1="0" x2="0" y2="1">
        <stop offset="0" stop-color="var(--city-light)"/>
        <stop offset="0.45" stop-color="var(--city-mid)"/>
        <stop offset="1" stop-color="var(--city-deep)"/>
      </linearGradient>
    </defs>

    <rect class="cover-background" width="523" height="740" fill="var(--slate)"/>

    <text class="brand-name" x="261.5" y="140" text-anchor="middle">NORTHGATE BUILDING SERVICES</text>

    <path class="accent-arc-top" d="M0 330 Q210 200 523 172 L523 182 Q220 212 0 340 Z" fill="var(--sky-blue)"/>
    <path class="white-band-top" d="M0 340 Q220 212 523 182 L523 200 Q230 222 0 352 Z" fill="var(--band-white)"/>

    <path class="city-skyline-photo" role="img" aria-label="Aerial photograph of a city skyline with high-rise towers"
          d="M0 352 Q230 222 523 200 L523 445 Q250 470 0 388 Z" fill="url(#cityTones)"/>

    <path class="white-band-bottom" d="M0 388 Q250 470 523 445 L523 462 Q250 490 0 398 Z" fill="var(--band-white)"/>
    <path class="accent-arc-bottom" d="M230 500 Q400 492 523 466 L523 476 Q400 503 230 504 Z" fill="var(--sky-blue)"/>

    <g class="values-statement">
      <text class="values-line" x="40" y="585">QUALITY</text>
      <text class="values-line" x="115" y="640">SERVICE</text>
      <text class="values-line" x="185" y="695">INTEGRITY</text>
    </g>
  </svg>
</main>
</body>
</html>
```